Ridgeline Security Solutions Trade Show

Backdrop for trade show and table cover. Colors to use are red, black and silver/grey . Logo attached. If you are able to view the website and pull any images, that would be great. Website is https://ridgelinesecuritygp.example/

```html
<!DOCTYPE html>
<html lang="en">
<head>
<meta charset="utf-8">
<title>Ridgeline Security Solutions – Trade Show Backdrop and Table Cover</title>
<link href="https://fonts.googleapis.com/css2?family=Oswald:wght@300;600;700&family=Poppins:wght@500;600;700;800&display=swap" rel="stylesheet">
<style>
  :root {
    --red: #e8202a;
    --red-deep: #c8161f;
    --navy: #171c33;
    --navy-mid: #1f2b4d;
    --silver: #c9ccd2;
    --silver-light: #eef0f2;
    --white: #ffffff;
    --ink: #14182b;
    --bg: #e3e4e6;
  }
  * { margin: 0; padding: 0; box-sizing: border-box; }
  html, body { width: 1200px; height: 1190px; overflow: hidden; }
  body { background: var(--bg); font-family: "Poppins", sans-serif; position: relative; }

  .backdrop {
    position: absolute; left: 40px; top: 24px;
    width: 1140px; height: 904px;
    transform: scale(0.9825); transform-origin: 0 0;
    background: var(--white); overflow: hidden;
    box-shadow: 0 18px 30px rgba(0,0,0,.18);
  }
  .backdrop-art { position: absolute; inset: 0; width: 1140px; height: 904px; }

  .brand { position: absolute; left: 224px; top: 150px; width: 240px; text-align: center; color: var(--red); }
  .brand-mark { width: 24px; height: 24px; border-radius: 50%; background: var(--red); margin: 0 auto 10px; }
  .brand-name { display: block; font-weight: 700; font-size: 30px; line-height: 1; letter-spacing: 1px; }
  .brand-sub { display: block; font-weight: 700; font-size: 11px; line-height: 1; letter-spacing: 2.4px; margin-top: 6px; }

  .headline { position: absolute; left: 52px; top: 278px; font-family: "Oswald", sans-serif; text-transform: uppercase; line-height: 1; }
  .headline-light { display: block; font-weight: 300; color: var(--white); font-size: 86px; letter-spacing: -1px; }
  .headline-accent { display: block; font-weight: 700; color: var(--red); font-size: 72px; margin-top: 10px; }
  .headline-strong { display: block; font-weight: 700; color: var(--white); font-size: 72px; margin-top: 12px; }

  .features { position: absolute; left: 60px; top: 568px; display: flex; gap: 16px; align-items: center; list-style: none; }
  .feature { display: flex; align-items: center; gap: 9px; color: var(--white); font-weight: 600; font-size: 18px; line-height: 1.1; }
  .feature svg { width: 54px; height: 58px; flex: none; }

  .call-tag { position: absolute; left: 288px; top: 683px; width: 196px; height: 34px; background: var(--red); color: var(--white); font-weight: 700; font-size: 21px; text-align: center; line-height: 34px; clip-path: polygon(8% 0, 92% 0, 100% 50%, 92% 100%, 8% 100%, 0 50%); }
  .phone-number { position: absolute; left: 236px; top: 716px; color: var(--white); font-weight: 700; font-size: 46px; line-height: 1.2; letter-spacing: .3px; }

  .website { position: absolute; left: 62px; top: 812px; font-weight: 800; font-size: 26px; color: var(--ink); letter-spacing: .3px; }
  .website .accent { color: var(--red); }

  .table-cover {
    position: absolute; left: 210px; top: 948px; width: 780px; height: 222px;
    background: linear-gradient(180deg, #e9353d, var(--red) 40%, var(--red-deep));
    color: var(--white); text-align: center;
  }
  .cover-row { display: flex; justify-content: space-around; padding: 18px 24px 0; }
  .cover-lockup { display: flex; align-items: center; gap: 8px; font-weight: 700; font-size: 15px; line-height: 1.1; text-align: left; }
  .cover-lockup .dot { width: 14px; height: 14px; border-radius: 50%; background: var(--white); }
  .cover-title { font-weight: 700; font-size: 62px; letter-spacing: 3px; margin-top: 20px; line-height: 1; }
  .cover-sub { font-weight: 600; font-size: 24px; letter-spacing: 6px; margin-top: 10px; }
</style>
</head>
<body>

<section class="backdrop">
  <svg class="backdrop-art" viewBox="0 0 1140 904">
    <defs>
      <linearGradient id="guardPhoto" x1="0" y1="0" x2="1" y2="1">
        <stop offset="0" stop-color="#5fb8c8"/>
        <stop offset=".45" stop-color="#1d4b5a"/>
        <stop offset="1" stop-color="#0d1f2a"/>
      </linearGradient>
      <linearGradient id="vehiclePhoto" x1="0" y1="0" x2="0" y2="1">
        <stop offset="0" stop-color="#4e6a45"/>
        <stop offset=".5" stop-color="#2a2d34"/>
        <stop offset="1" stop-color="#6b6d70"/>
      </linearGradient>
      <linearGradient id="silverRim" x1="0" y1="0" x2="1" y2="1">
        <stop offset="0" stop-color="#f4f5f7"/>
        <stop offset=".5" stop-color="#9da1a8"/>
        <stop offset="1" stop-color="#e6e8eb"/>
      </linearGradient>
      <linearGradient id="phoneBar" x1="0" y1="0" x2="1" y2="0">
        <stop offset="0" stop-color="#1c2240"/>
        <stop offset=".5" stop-color="#1f4a8a"/>
        <stop offset="1" stop-color="#1c2240"/>
      </linearGradient>
    </defs>

    <g fill="none" stroke="#e7e8ea" stroke-width="2">
      <circle cx="344" cy="184" r="170"/>
      <circle cx="344" cy="184" r="138" stroke-width="10" stroke="#eff0f1"/>
      <circle cx="68" cy="84" r="26"/>
      <circle cx="610" cy="92" r="30"/>
      <circle cx="676" cy="720" r="26"/>
      <circle cx="990" cy="820" r="130" stroke-width="10" stroke="#f0f1f2"/>
      <path d="M0 84 H42 M640 92 L720 10 H1140 M545 185 H660 L700 150"/>
    </g>
    <circle cx="247" cy="8" r="6" fill="#9a9ea6"/>
    <circle cx="344" cy="184" r="124" fill="var(--white)"/>

    <rect x="0" y="256" width="680" height="290" fill="var(--navy)"/>
    <rect x="0" y="545" width="680" height="113" fill="var(--red)"/>

    <path d="M1012 50 C900 128 780 150 655 148 C640 440 720 660 1012 808 L1160 740 V120 C1100 110 1060 90 1012 50 Z" fill="var(--navy)"/>
    <path d="M1012 66 C905 138 790 160 672 162 C660 440 735 650 1012 792 L1150 730 V128 C1095 118 1058 100 1012 66 Z" fill="url(#silverRim)"/>
    <g role="img" aria-label="Photo of a uniformed security guard seen from behind, jacket printed SECURITY">
      <path d="M1012 100 C915 160 812 180 704 183 C695 440 760 630 1012 756 L1150 690 V140 C1090 132 1055 120 1012 100 Z" fill="url(#guardPhoto)"/>
    </g>

    <path d="M776 380 C720 420 650 436 588 436 C588 600 640 700 776 752 C912 700 964 600 964 436 C902 436 832 420 776 380 Z" fill="var(--white)"/>
    <path d="M776 392 C722 430 660 446 600 446 C600 600 650 694 776 742 C902 694 952 600 952 446 C892 446 830 430 776 392 Z" fill="var(--navy)"/>
    <path d="M776 404 C726 440 668 456 614 456 C614 600 660 686 776 730 C892 686 938 600 938 456 C884 456 826 440 776 404 Z" fill="url(#silverRim)"/>
    <g role="img" aria-label="Photo of a black and red company patrol vehicle parked under trees">
      <path d="M776 426 C730 458 680 470 636 470 C638 598 678 672 776 712 C874 672 914 598 916 470 C872 470 822 458 776 426 Z" fill="url(#vehiclePhoto)"/>
    </g>

    <polygon points="205,698 618,698 636,744 618,790 205,790" fill="url(#phoneBar)"/>
    <polygon points="150,698 190,698 220,744 190,790 150,790 180,744" fill="var(--red)"/>
    <polygon points="180,698 200,698 230,744 200,790 180,790 210,744" fill="var(--navy)"/>
    <polygon points="86,700 142,700 170,744 142,788 86,788 58,744" fill="var(--navy)"/>
    <polygon points="90,708 138,708 160,744 138,780 90,780 68,744" fill="var(--red)"/>
    <path d="M100 730 c4 -4 8 -4 10 0 l4 8 c1 3 0 5 -2 6 l-3 2 c3 7 8 12 15 15 l2 -3 c1 -2 3 -3 6 -2 l8 4 c4 2 4 6 0 10 c-4 4 -10 5 -16 2 c-12 -6 -20 -14 -26 -26 c-3 -6 -2 -12 2 -16 Z" fill="var(--white)"/>
    <path d="M124 724 a16 16 0 0 1 14 14 M122 732 a8 8 0 0 1 8 8" fill="none" stroke="var(--white)" stroke-width="3" stroke-linecap="round"/>

    <circle cx="736" cy="830" r="27" fill="var(--navy)"/>
    <circle cx="814" cy="830" r="27" fill="var(--navy)"/>
    <circle cx="892" cy="830" r="27" fill="var(--navy)"/>
  </svg>

  <div class="brand">
    <div class="brand-mark"></div>
    <span class="brand-name">RIDGELINE</span>
    <span class="brand-sub">SECURITY SOLUTIONS</span>
  </div>

  <h1 class="headline">
    <span class="headline-light">Exceptional</span>
    <span class="headline-accent">Security Guard</span>
    <span class="headline-strong">Solutions</span>
  </h1>

  <ul class="features">
    <li class="feature">
      <svg viewBox="0 0 64 68"><path d="M32 2 L60 12 C60 40 50 56 32 66 C14 56 4 40 4 12 Z" fill="var(--navy)" stroke="var(--silver)" stroke-width="3"/><circle cx="32" cy="32" r="14" fill="none" stroke="var(--white)" stroke-width="2.5"/><path d="M32 24 V32 L38 36" stroke="var(--white)" stroke-width="2.5" fill="none" stroke-linecap="round"/></svg>
      <span>24/7<br>Availability</span>
    </li>
    <li class="feature">
      <svg viewBox="0 0 64 68"><path d="M32 2 L60 12 C60 40 50 56 32 66 C14 56 4 40 4 12 Z" fill="var(--navy)" stroke="var(--silver)" stroke-width="3"/><circle cx="32" cy="26" r="6" fill="none" stroke="var(--white)" stroke-width="2.5"/><path d="M20 46 C20 36 44 36 44 46" stroke="var(--white)" stroke-width="2.5" fill="none"/></svg>
      <span>Highly<br>Trained</span>
    </li>
    <li class="feature">
      <svg viewBox="0 0 64 68"><path d="M32 2 L60 12 C60 40 50 56 32 66 C14 56 4 40 4 12 Z" fill="var(--navy)" stroke="var(--silver)" stroke-width="3"/><circle cx="32" cy="34" r="13" fill="none" stroke="var(--white)" stroke-width="2.5"/><path d="M28 18 H36 M34 27 L28 36 H35 L30 42" stroke="var(--white)" stroke-width="2.5" fill="none" stroke-linecap="round"/></svg>
      <span>Rapid<br>Response<br>Times</span>
    </li>
  </ul>

  <div class="call-tag">CALL US NOW</div>
  <div class="phone-number">(555) 014-2718</div>

  <div class="website">WWW.<span class="accent">RIDGELINESECURITYGP</span>.EXAMPLE</div>
</section>

<section class="table-cover">
  <div class="cover-row">
    <div class="cover-lockup"><span class="dot"></span><span>RIDGELINE<br>SECURITY SOLUTIONS</span></div>
    <div class="cover-lockup"><span class="dot"></span><span>RIDGELINE<br>SECURITY SOLUTIONS</span></div>
    <div class="cover-lockup"><span class="dot"></span><span>RIDGELINE<br>SECURITY SOLUTIONS</span></div>
  </div>
  <div class="cover-title">RIDGELINE</div>
  <div class="cover-sub">SECURITY SOLUTIONS</div>
</section>

</body>
</html>
```